Webshop Template

For our Webstore in UK we need a complete Template,
shoppingcart is Magento, the Shop is focussed on Download software,

the name: Appvaultdepot.co.uk

Check out some other good stores, like lumawerk.de

for example the Page from 

www.brenvik.co.uk or

www.lumawerk.de

www.tastenhugo.de

www.klickrabatt.de

The Logodesign which are in Consideration

http://www.artmosaiq.com/design/5520817/logo-design-by-tomasz7kv

http://www.artmosaiq.com/design/5518360/logo-design-by-luisgaviota

http://www.artmosaiq.com/design/5517245/logo-design-by-kestrel-works

http://www.artmosaiq.com/design/5516093/logo-design-by-zumbiloft

http://www.artmosaiq.com/design/5515471/logo-design-by-tivaro

http://www.artmosaiq.com/design/5514902/logo-design-by-blue-fern-graphics-

Target Market(s)

B2C - Consumer Marcet

Industry/Entity Type

Shop

```html
<!DOCTYPE html>
<html lang="en">
<head>
<meta charset="utf-8">
<title>Appvaultdepot – Webshop</title>
<link href="https://fonts.googleapis.com/css2?family=Arimo:wght@400;700&family=Open+Sans:wght@400;600&display=swap" rel="stylesheet">
<style>
:root{
  --page:#f7f7f8;
  --text:#333;
  --muted:#555;
  --blue:#0a82c8;
  --blue-light:#1aa3ec;
  --orange:#f05a1a;
  --orange-light:#ff8a2a;
  --dark:#2e2e2e;
  --line:#dcdcdc;
  --brand-grey:#a9a9a9;
  --footer:#f3f3f3;
}
*{box-sizing:border-box;margin:0;padding:0}
html,body{width:999px;height:1200px;overflow:hidden}
body{background:var(--page);font-family:Arimo,Arial,sans-serif;color:var(--text);position:relative}
.abs{position:absolute}
.logo{left:107px;top:14px;display:flex;align-items:center;gap:8px}
.logo-mark{width:40px;height:40px;border-radius:50%;background:var(--blue)}
.logo-name{font-size:27px;color:#3a3a3a;letter-spacing:-0.5px}
.top-links{right:114px;top:18px;font-size:10.5px;color:var(--muted);word-spacing:2px}
.search{left:635px;top:52px;display:flex}
.search-input{width:191px;height:26px;border:1px solid #ccc;background:#fff}
.search-btn{width:57px;height:26px;border:1px solid #ccc;background:#f0f0f0;font-size:10.5px;font-weight:700;color:#444;display:flex;align-items:center;justify-content:center;margin-left:2px}
.nav{left:102px;top:97px;width:793px;height:41px;border-radius:4px;background:linear-gradient(#1ba5ef,#0a82cc)}
.nav a{position:absolute;top:13px;color:#fff;font-weight:700;font-size:12px;text-decoration:none}
.nav .sep{position:absolute;top:6px;width:1px;height:29px;background:rgba(255,255,255,.25)}
.banner{left:105px;top:162px;width:790px;height:352px;background:linear-gradient(90deg,#f0f0f0,#fafafa 60%,#fff);border:1px solid #eee;border-bottom:2px solid #888}
.banner-art{left:53px;top:29px;width:283px;height:309px;background:linear-gradient(135deg,#3b3b3b,#1c5fa8 55%,#e6e6e6)}
.banner-bar{left:0;bottom:-2px;width:78px;height:2px;background:var(--blue)}
.banner h2{left:399px;top:83px;font-family:Verdana,sans-serif;font-size:28px;color:var(--blue);letter-spacing:1px;font-weight:700}
.banner p{left:399px;top:124px;width:290px;font-size:11px;line-height:15px;color:#222}
.shop-btn{left:399px;top:190px;width:168px;height:44px;border-radius:22px;background:linear-gradient(var(--orange-light),#e8560d);color:#fff;font-weight:700;font-size:17px;display:flex;align-items:center;padding-left:19px}
.shop-btn span.cart{position:absolute;right:-3px;top:-2px;width:48px;height:48px;border-radius:50%;background:#e24a0c;border:2px solid #fff}
.pager{left:693px;top:317px;display:flex;gap:2px}
.pager span{width:14px;height:14px;font-size:10px;font-weight:700;display:flex;align-items:center;justify-content:center;background:#e8e8e8;color:#222}
.pager .on{background:#222;color:#fff}
.brands{top:545px;left:105px;width:790px;height:20px}
.brands span{position:absolute;transform:translateX(-50%);font-weight:700;font-size:15px;color:var(--brand-grey);letter-spacing:.5px}
.section-bar{left:104px;top:594px;width:788px;height:32px;background:#fff;border:1px solid var(--line);border-left:6px solid #333;font-size:11.5px;padding:10px 0 0 11px;color:#222}
.dots{right:12px;top:12px;display:flex;gap:8px}
.dots i{width:8px;height:8px;border-radius:50%;background:#ddd;display:block}
.dots i.on{background:#333}
.arrow{top:740px;font-size:40px;color:#ccc;font-family:Arial,sans-serif}
.card{top:642px;width:205px;height:274px;background:#fff;box-shadow:0 0 4px rgba(0,0,0,.18);text-align:center}
.card-art{margin:12px auto 0;width:110px;height:155px;background:linear-gradient(135deg,#2a2a2a,#3d7a3a 45%,#f0c020 70%,#2a2a2a)}
.card h3{font-family:'Open Sans',sans-serif;font-weight:400;font-size:14.5px;color:var(--orange);margin-top:17px}
.card .price{font-family:'Open Sans',sans-serif;font-size:17.5px;color:var(--orange);margin-top:4px}
.card .btns{display:flex;justify-content:center;gap:5px;margin-top:10px}
.btn-cart{width:76px;height:25px;background:var(--dark);color:#fff;font-size:10.5px;font-weight:700;display:flex;align-items:center;justify-content:center}
.btn-details{width:56px;height:25px;background:#e4e4e4;color:#444;font-size:10.5px;font-weight:700;display:flex;align-items:center;justify-content:center}
.footer{left:0;top:953px;width:999px;height:247px;background:var(--footer);border-top:1px solid #ddd}
.col{top:18px}
.col h4{font-size:11px;font-weight:700;color:#333;margin-bottom:10px}
.col li{list-style:none;font-size:10px;color:#555;line-height:18.3px}
.addr{font-size:10px;color:#555;line-height:17px}
.phone{font-size:12px;color:var(--orange);margin-top:10px}
.payments{left:666px;top:38px;display:grid;grid-template-columns:repeat(3,37px);gap:4px 5px}
.payments span{height:25px;border:1px solid #ccc;border-radius:2px;background:#fff;font-size:7.5px;color:#333;display:flex;align-items:center;justify-content:center}
.rule{left:115px;top:193px;width:791px;height:1px;background:#ccc}
.copy{left:115px;top:210px;font-size:10px;color:#333}
.follow{left:683px;top:213px;display:flex;align-items:center;gap:7px;font-size:10.5px;color:#333}
.follow .net{width:25px;height:25px;background:#3a6fb0;color:#fff;font-size:6px;display:flex;align-items:center;justify-content:center}
</style>
</head>
<body>
<header>
  <div class="abs logo"><span class="logo-mark"></span><span class="logo-name">appvaultdepot</span></div>
  <div class="abs top-links">My Account &nbsp;|&nbsp; My Cart &nbsp;|&nbsp; Checkout &nbsp;|&nbsp; My Wishlist &nbsp;|&nbsp; Log In</div>
  <div class="abs search"><div class="search-input"></div><div class="search-btn">Search</div></div>
  <nav class="abs nav">
    <a style="left:25px">Home</a><i class="sep" style="left:79px"></i>
    <a style="left:101px">Downloads</a><i class="sep" style="left:186px"></i>
    <a style="left:208px">Reviews</a><i class="sep" style="left:277px"></i>
    <a style="left:299px">Forum</a><i class="sep" style="left:358px"></i>
    <a style="left:379px">About</a><i class="sep" style="left:437px"></i>
    <a style="left:457px">Contacts</a>
  </nav>
</header>

<section class="abs banner">
  <div class="abs banner-art" role="img" aria-label="Two software product boxes labelled Software 6.0"></div>
  <h2 class="abs">Effective Software</h2>
  <p class="abs">Simply dummy text of the printing and typesetting industry. Lorem Ipsum has been the industry's standard dummy text ever since the 1500s</p>
  <div class="abs shop-btn">SHOP NOW<span class="cart"></span></div>
  <div class="abs pager"><span>1</span><span>2</span><span class="on">3</span><span>4</span><span>5</span></div>
  <div class="abs banner-bar"></div>
</section>

<div class="abs brands">
  <span style="left:41px">Pomaro</span><span style="left:124px">Kestra</span><span style="left:209px">Velnix</span><span style="left:318px">Brenvik</span><span style="left:425px">Ondaro</span><span style="left:534px">Hikarune</span><span style="left:643px">Solvani</span><span style="left:736px">Quell</span>
</div>

<div class="abs section-bar">NEW PRODUCTS<div class="abs dots"><i></i><i></i><i class="on"></i></div></div>

<div class="abs arrow" style="left:106px">&#10216;</div>
<div class="abs arrow" style="left:857px">&#10217;</div>

<article class="abs card" style="left:141px"><div class="card-art" role="img" aria-label="Software pack product box"></div><h3>Standard Soft Package</h3><div class="price">$273.89</div><div class="btns"><span class="btn-cart">Add to Cart</span><span class="btn-details">Details</span></div></article>
<article class="abs card" style="left:389px"><div class="card-art" role="img" aria-label="Software pack product box"></div><h3>Standard Soft Package</h3><div class="price">$273.89</div><div class="btns"><span class="btn-cart">Add to Cart</span><span class="btn-details">Details</span></div></article>
<article class="abs card" style="left:635px"><div class="card-art" role="img" aria-label="Software pack product box"></div><h3>Standard Soft Package</h3><div class="price">$273.89</div><div class="btns"><span class="btn-cart">Add to Cart</span><span class="btn-details">Details</span></div></article>

<footer class="abs footer">
  <div class="abs col" style="left:115px"><h4>Information</h4><ul><li>About Us</li><li>Customer Service</li><li>Privacy Policy</li><li>Site Map</li><li>Search Terms</li><li>Advanced Search</li><li>Orders and Returns</li><li>Contact Us</li></ul></div>
  <div class="abs col" style="left:248px"><h4>Why buy from us</h4><ul><li>Shipping &amp; Returns</li><li>Secure Shopping</li><li>International Shipping</li><li>Affiliates</li><li>Group Sales</li></ul></div>
  <div class="abs col" style="left:381px"><h4>My account</h4><ul><li>Sign In</li><li>View Cart</li><li>My Wishlist</li><li>Track My Order</li><li>Help</li></ul></div>
  <div class="abs col" style="left:515px"><h4>Store Location</h4><div class="addr">4127 Kelvin Lane,<br>Glasgow, G12 7QX</div><h4 style="margin-top:12px">Order online</h4><div class="phone">1 800 555-0142</div></div>
  <div class="abs col" style="left:668px;top:20px"><h4>Easy payment</h4></div>
  <div class="abs payments"><span>Payvo</span><span>Cirqa</span><span>Sendly</span><span>Amberline</span><span>Billo</span><span>Trakko</span></div>
  <div class="abs rule"></div>
  <div class="abs copy">Copyright © 2012 appvaultdepot. All Rights Reserved.</div>
  <div class="abs follow">Follow us <span class="net" style="margin-left:8px">Frendo</span><span class="net">Chirpa</span><span class="net" style="background:#d9452f">Plusio</span><span class="net" style="background:#c62828">Vidra</span></div>
</footer>
</body>
</html>
```